Financial management business is partnering with chef for a cooking demo and financial workshop j...

We need an promotional invitation/postcard to our event called "Lanterns on the Porch: An Evening Among Old Friends."

Target Market(s)

55+, seniors

Font styles to use
Serif

Requirements
Must have
• EDDM formatting 6"x9"

```html
<!DOCTYPE html>
<html lang="en">
<head>
<meta charset="utf-8">
<title>Lanterns on the Porch – Event Postcard</title>
<link rel="stylesheet" href="https://fonts.googleapis.com/css2?family=Archivo:wght@400;600;700;800;900&family=Montserrat:wght@300;400&display=swap">
<style>
  :root {
    --page-bg: #bcbdbf;
    --maroon: #6b1035;
    --navy: #2f3190;
    --ink: #1e1e1e;
    --panel: #f0f0f0;
    --white: #ffffff;
    --rule: #c9c9c9;
  }
  * { margin: 0; padding: 0; box-sizing: border-box; }
  html, body { width: 903px; height: 1200px; overflow: hidden; }
  body { background: var(--page-bg); font-family: "Archivo", sans-serif; color: var(--ink); position: relative; }

  .card { position: absolute; left: 118px; width: 668px; height: 474px; overflow: hidden; }
  .card--front { top: 115px; }
  .card--back { top: 611px; background: var(--white); }

  /* Front */
  .hero-photo { position: absolute; inset: 0;
    background:
      radial-gradient(ellipse 38% 42% at 72% 58%, rgba(196,140,80,.85), rgba(196,140,80,0) 70%),
      radial-gradient(ellipse 30% 30% at 80% 20%, rgba(200,80,80,.75), rgba(200,80,80,0) 70%),
      linear-gradient(180deg, rgba(0,0,0,0) 55%, rgba(110,140,50,.9) 100%),
      linear-gradient(90deg, #7a2350 0%, #8a3a5e 35%, #a35a4f 60%, #b98a60 100%);
  }
  .headline { position: absolute; left: 36px; top: 40px; color: var(--white);
    font-weight: 900; font-size: 46px; line-height: 46px; letter-spacing: -2.2px; width: 420px; }
  .subhead { position: absolute; left: 42px; top: 146px; color: var(--white);
    font-family: "Montserrat", sans-serif; font-weight: 300; font-size: 19px; line-height: 21px; letter-spacing: 1.6px; text-transform: uppercase; }
  .title-rule { position: absolute; left: 42px; top: 196px; width: 280px; height: 5px; background: var(--white); }
  .event-when, .event-where { position: absolute; top: 206px; color: var(--white); font-size: 15px; line-height: 19px; }
  .event-when { left: 42px; font-weight: 700; }
  .event-when sup { font-size: 9px; }
  .event-where { left: 205px; }
  .event-where .label { font-family: "Montserrat", sans-serif; font-weight: 400; }
  .event-where .venue { font-weight: 700; }

  .sponsor { position: absolute; left: 399px; top: 363px; width: 245px; height: 87px;
    background: var(--white); border-top-right-radius: 60px 80px; border-bottom-right-radius: 0; padding: 8px 14px; }
  .sponsor-label { font-size: 9.5px; font-weight: 700; color: #333; }
  .sponsor-mark { display: flex; align-items: center; gap: 10px; margin-top: 14px; }
  .sponsor-mark .dot { width: 26px; height: 26px; background: var(--navy); }
  .sponsor-mark .name { font-size: 22px; font-weight: 600; color: var(--navy); line-height: 24px; }

  /* Back */
  .kitchen-photo { position: absolute; left: 0; top: 0; }
  .stamp-box { position: absolute; left: 523px; top: 13px; width: 114px; height: 98px; border: 1px solid var(--rule); }
  .address-line { position: absolute; height: 1px; background: var(--rule); right: 31px; }

  .info-panel { position: absolute; left: 0; top: 253px; width: 668px; height: 221px; background: var(--panel); }
  .bio-photo { position: absolute; left: 5px; width: 113px; height: 90px; border-radius: 45px 0 0 45px; }
  .bio-photo--planner { top: 10px; background: linear-gradient(135deg, #8a9a7a, #3f4a5a); }
  .bio-photo--chef { top: 119px; background: linear-gradient(135deg, #9a8f85, #4a3c36); }
  .bio { position: absolute; left: 123px; width: 249px; font-size: 9.2px; line-height: 11.4px; text-align: justify; }
  .bio--planner { top: 13px; }
  .bio--chef { top: 122px; }
  .bio h3 { font-size: 9.4px; font-weight: 700; color: var(--maroon); line-height: 11.4px; text-align: left; }

  .panel-divider { position: absolute; left: 382px; top: 12px; width: 1px; height: 200px; background: var(--maroon); }
  .event-summary { position: absolute; left: 389px; top: 10px; width: 256px; }
  .event-summary h2 { font-size: 15.5px; line-height: 19px; font-weight: 700; color: var(--maroon); }
  .event-summary p { font-size: 9.2px; line-height: 11.4px; margin-top: 10px; }
  .event-summary .raffle { font-weight: 700; color: var(--maroon); margin-top: 14px; }
  .partner-mark { display: flex; align-items: center; gap: 6px; margin-top: 10px; }
  .partner-mark .dot { width: 18px; height: 18px; border-radius: 50%; background: var(--maroon); }
  .partner-mark .name { font-size: 9px; font-weight: 700; color: var(--ink); text-transform: uppercase; }
</style>
</head>
<body>

<section class="card card--front">
  <div class="hero-photo" role="img" aria-label="Picnic basket with grapes, wine and bread on grass, friends blurred in the background"></div>
  <h1 class="headline">Lanterns on the Porch</h1>
  <p class="subhead">An Evening Among<br>Old Friends</p>
  <div class="title-rule"></div>
  <p class="event-when">Tuesday, July 23<sup>rd</sup><br>@ 12:30 p.m.</p>
  <p class="event-where"><span class="label">WHERE:</span><br><span class="venue">Whitfield Hall</span></p>
  <div class="sponsor">
    <p class="sponsor-label">Sponsored by Harlow Financial</p>
    <div class="sponsor-mark"><span class="dot"></span><span class="name">Harlow Financial</span></div>
  </div>
</section>

<section class="card card--back">
  <svg class="kitchen-photo" width="424" height="253" viewBox="0 0 424 253" role="img" aria-label="Chef preparing vegetables at a kitchen island while a senior woman watches">
    <defs>
      <linearGradient id="kitchenTone" x1="0" y1="0" x2="1" y2="1">
        <stop offset="0" stop-color="#e6e4df"/>
        <stop offset=".55" stop-color="#b7b2aa"/>
        <stop offset="1" stop-color="#3a3a3c"/>
      </linearGradient>
    </defs>
    <path d="M0 0 H424 C420 130 370 225 276 253 H0 Z" fill="url(#kitchenTone)"/>
  </svg>
  <div class="stamp-box"></div>
  <div class="address-line" style="top:141px; left:441px;"></div>
  <div class="address-line" style="top:162px; left:416px;"></div>
  <div class="address-line" style="top:184px; left:399px;"></div>
  <div class="address-line" style="top:205px; left:387px;"></div>
  <div class="address-line" style="top:226px; left:374px;"></div>

  <div class="info-panel">
    <div class="bio-photo bio-photo--planner" role="img" aria-label="Portrait of the financial planner"></div>
    <div class="bio bio--planner">
      <h3>A Certified Financial Planner you can trust.</h3>
      <p>Walt Harlow is a Certified Financial Planner, specializing in asset management of IRA, retirement, investment, and trust accounts. Harlow Advisors, LLC is an independent Registered Investment Advisor with low cost, commission free business model. Concierge level service is provided to Maple Ridge residents.</p>
    </div>

    <div class="bio-photo bio-photo--chef" role="img" aria-label="Portrait of the chef"></div>
    <div class="bio bio--chef">
      <h3>Chef Dean Ashby</h3>
      <p>Chef Dean Ashby is a formally trained chef with over 15 years of experience. He started Hearth Table Kitchens Brookhaven, a meal service that connects seniors with licensed, professional chefs who prepare high-quality, affordable, and nutritious meals in the home. Dean is so pleased to have found an opportunity to share his passion for food and connect with local Seniors.</p>
    </div>

    <div class="panel-divider"></div>
    <div class="event-summary">
      <h2>Lanterns on the Porch: An Evening Among Old Friends</h2>
      <p>Learn from Chef Dean Ashby how to build a menu full of flavor, nutrition, and seasonal ingredients with ease. Followed by a financial workshop where Walt Harlow, Certified Financial Planner, will have some fresh investment ideas to go along with your farm-to-table meal. Walt encourages any questions you may have</p>
      <p class="raffle">Enter a raffle to win the services of Chef Dean who will work with you to design a meal plan of 10-12 servings that addresses your dietary needs.</p>
      <div class="partner-mark"><span class="dot"></span><span class="name">Hearth Table</span></div>
    </div>
  </div>
</section>

</body>
</html>
```